Boutique Fitness Facility needs a new meal plan design that is as hot as our workouts!

We are about to host our 6 week Heatwave Reset program and we need to have a great looking meal plan handout created that we can give to all of our participants.

I have attached an example of our current full meal plan, for a reference only.

As in the example I've provided, I'd like to have certain areas color coded such as the proteins being Blue, Fats -yellow, Carbs - orange and veggies- green.

These colors will corollate to the Breakfast - snack - lunch - snack - Dinner graph that I've provided and would like to have added to the new handout.

I would like our logo placed at the top and beneath the logo have the text "Heatwave Reset Challenge"

The flyer should be of a summer influence in colors and design and
All text should be easy to read.

Thank you and I look forward to seeing your design!

```html
<!DOCTYPE html>
<html lang="en">
<head>
<meta charset="utf-8">
<title>Heatwave Reset Challenge – Meal Plan</title>
<link href="https://fonts.googleapis.com/css2?family=Bangers&family=Poppins:wght@400;600;700;800&display=swap" rel="stylesheet">
<style>
  :root{
    --page:#d9d9d9;
    --sand:#f8ecc6;
    --ink:#1d1d1d;
    --panel:#262626;
    --protein:#2f4aa8;
    --veg:#2f9b45;
    --fat:#f2cc10;
    --carb:#ef8a1a;
    --sea:#17b3c4;
    --shore:#efb598;
    --leaf:#3f9a3c;
    --white:#ffffff;
  }
  *{box-sizing:border-box;margin:0;padding:0}
  html,body{width:1200px;height:1200px;overflow:hidden;background:var(--page)}
  body{font-family:"Poppins",sans-serif;color:var(--ink)}
  .flyer{position:absolute;left:185px;top:25px;width:830px;height:1150px;background:var(--sand);overflow:hidden;box-shadow:0 18px 40px rgba(0,0,0,.25)}
  .leaf{position:absolute;border-radius:50%;background:radial-gradient(circle,#5cb34f,var(--leaf) 70%,transparent 72%);opacity:.85}
  .leaf.tl{left:-60px;top:-50px;width:200px;height:150px}
  .leaf.tr{right:-60px;top:-40px;width:210px;height:160px}
  .leaf.ml{left:-50px;top:640px;width:110px;height:130px}
  .leaf.mr{right:-40px;top:790px;width:100px;height:120px}
  .brand{position:absolute;left:315px;top:22px;width:200px;height:70px;background:linear-gradient(#2b2b2b,#0c0c0c);display:flex;align-items:center;justify-content:center;gap:8px}
  .brand-name{font-family:"Poppins",sans-serif;font-weight:800;font-size:28px;color:var(--fat)}
  .brand-dot{width:12px;height:12px;border-radius:50%;background:var(--fat)}
  .title{position:absolute;left:0;right:0;top:100px;text-align:center;font-family:"Bangers",cursive;font-size:66px;letter-spacing:2px;color:var(--ink);-webkit-text-stroke:2px var(--fat);text-shadow:4px 4px 0 var(--fat)}
  .card{position:absolute;background:var(--white);border-radius:10px;box-shadow:0 4px 10px rgba(0,0,0,.18);padding:46px 14px 16px}
  .card .tab{position:absolute;top:-14px;left:50%;transform:translateX(-50%);padding:6px 28px;border-radius:0 0 14px 14px;color:var(--white);font-weight:700;font-size:20px;letter-spacing:1px;white-space:nowrap}
  .card .bar{position:absolute;bottom:0;left:30px;right:30px;height:6px;border-radius:6px 6px 0 0}
  .card ul{list-style:none}
  .card li{font-weight:600;font-size:14px;line-height:1.75;display:flex;align-items:center;gap:8px;white-space:nowrap}
  .card li::before{content:"";width:9px;height:9px;border-radius:50%;flex:none;background:var(--c)}
  .protein{--c:var(--protein);left:30px;top:200px;width:260px;height:405px}
  .veg{--c:var(--veg);left:305px;top:225px;width:260px;height:225px}
  .fat{--c:var(--fat);left:305px;top:475px;width:260px;height:160px}
  .fat li{line-height:1.5;white-space:normal;align-items:flex-start}
  .fat li::before{margin-top:6px}
  .carb{--c:var(--carb);left:580px;top:240px;width:225px;height:395px}
  .portion{position:absolute;display:flex;align-items:center;background:var(--white);border-radius:20px;box-shadow:0 2px 6px rgba(0,0,0,.15);font-weight:600;font-size:14px}
  .portion b{background:var(--ink);color:var(--fat);border-radius:20px;padding:5px 12px;font-size:13px}
  .portion span{padding:5px 16px}
  .portion.small{left:40px;top:620px}
  .portion.large{left:430px;top:650px}
  .plan{position:absolute;left:25px;top:690px;width:780px;height:210px;background:var(--panel);border:4px solid var(--fat);border-radius:8px;color:var(--white)}
  .plan svg{position:absolute;left:20px;top:8px}
  .plan-copy{position:absolute;left:0;right:0;bottom:14px;text-align:center;font-weight:600;font-size:15px;line-height:1.45}
  .beach{position:absolute;left:0;right:0;top:900px;bottom:0;background:linear-gradient(170deg,var(--shore) 0 35%,var(--sea) 36%)}
  .lead{position:absolute;left:0;right:0;top:912px;text-align:center;font-weight:700;font-size:14px;letter-spacing:2px;color:var(--ink)}
  .tip{position:absolute;background:var(--white);padding:8px 12px 10px;box-shadow:0 3px 6px rgba(0,0,0,.2);clip-path:polygon(0 6%,8% 0,30% 4%,55% 0,80% 5%,100% 0,98% 50%,100% 96%,75% 100%,50% 95%,25% 100%,0 96%,2% 50%)}
  .tip h3{font-weight:800;font-size:16px;line-height:1.1}
  .tip p{font-size:10px;line-height:1.3;margin-top:4px}
  .t1{left:25px;top:938px;width:245px}
  .t2{left:285px;top:938px;width:260px}
  .t3{left:560px;top:938px;width:245px}
  .t4{left:60px;top:1058px;width:320px}
  .t5{left:410px;top:1058px;width:360px}
</style>
</head>
<body>
<main class="flyer">
  <div class="leaf tl" role="img" aria-label="Palm leaf decoration"></div>
  <div class="leaf tr" role="img" aria-label="Palm leaf decoration"></div>
  <div class="leaf ml" role="img" aria-label="Monstera leaf decoration"></div>
  <div class="leaf mr" role="img" aria-label="Monstera leaf decoration"></div>

  <div class="brand"><span class="brand-dot"></span><span class="brand-name">PulseForge</span></div>
  <h1 class="title">Heatwave Reset Challenge</h1>

  <section class="card protein">
    <div class="tab" style="background:var(--protein)">PROTEIN</div>
    <ul>
      <li>4-6oz Chicken Breast</li><li>4-6oz Turkey Breast</li><li>4-6oz Filet Mignon</li>
      <li>4-6oz Flank Steak</li><li>4-6oz Salmon</li><li>4-6oz Tuna</li><li>4-6oz Cod</li>
      <li>4-6oz Cottage Cheese</li><li>4-6oz Greek Yogurt</li><li>4-6oz Tofu</li>
      <li>3-5 egg whites + 1 whole egg</li>
    </ul>
    <div class="bar" style="background:var(--protein)"></div>
  </section>

  <section class="card veg">
    <div class="tab" style="background:var(--veg)">VEGETABLES</div>
    <ul>
      <li>1 Scoop Powdered Greens</li><li>1 Cup Sautéed Spinach</li><li>1 Cup Sautéed Kale, Broccoli</li>
      <li>1 Cup Sautéed Bell Pepper</li><li>1 Cup Sautéed Carrots</li><li>1 Cup Sautéed Zucchini</li>
    </ul>
    <div class="bar" style="background:var(--veg)"></div>
  </section>

  <section class="card fat">
    <div class="tab" style="background:var(--fat);color:var(--ink)">FAT</div>
    <ul>
      <li>1/4 - 1/2 Avocado</li><li>1 tbs Olive Oil</li><li>1 small handful Almonds, Walnuts, Cashews</li>
    </ul>
    <div class="bar" style="background:var(--fat)"></div>
  </section>

  <section class="card carb">
    <div class="tab" style="background:var(--carb)">CARBS</div>
    <ul>
      <li>3-4oz Sweet Potato</li><li>1/4-1/2 cup White Rice</li><li>1/4-1/2 cup Quinoa</li>
      <li>1/4-1/2 cup Oatmeal</li><li>3/4 cup Blueberries</li><li>3/4 cup Strawberries</li>
      <li>3/4 cup Raspberries</li><li>1 med. Apple</li><li>1 small orange</li><li>1 small grapefruit</li>
    </ul>
    <div class="bar" style="background:var(--carb)"></div>
  </section>

  <div class="portion small"><b>&lt; 150 lbs</b><span>Stick to Smaller Portions</span></div>
  <div class="portion large"><b>&gt; 150 lbs</b><span>Stick to Larger Portions</span></div>

  <section class="plan">
    <svg width="740" height="120" viewBox="0 0 740 120" font-family="Poppins, sans-serif">
      <defs>
        <marker id="arrow" markerWidth="8" markerHeight="8" refX="6" refY="4" orient="auto"><path d="M0 0L8 4L0 8Z" fill="#4d7fd6"/></marker>
      </defs>
      <g transform="translate(120 60) rotate(-90)">
        <circle r="42" fill="none" stroke="var(--carb)" stroke-width="16" stroke-dasharray="86 178"/>
        <circle r="42" fill="none" stroke="var(--protein)" stroke-width="16" stroke-dasharray="86 178" stroke-dashoffset="-88"/>
        <circle r="42" fill="none" stroke="var(--veg)" stroke-width="16" stroke-dasharray="86 178" stroke-dashoffset="-176"/>
        <circle r="32" fill="#b5b5b5"/>
      </g>
      <text x="120" y="64" text-anchor="middle" font-size="10" font-weight="700" fill="#fff">BREAKFAST</text>
      <path d="M180 45 Q205 25 230 45" fill="none" stroke="#4d7fd6" stroke-width="4" marker-end="url(#arrow)"/>
      <rect x="178" y="55" width="70" height="20" fill="var(--veg)"/>
      <text x="213" y="69" text-anchor="middle" font-size="11" font-weight="800" fill="#fff">SNACK</text>
      <text x="213" y="90" text-anchor="middle" font-size="10" fill="#ccc">1/2 Portion</text>
      <text x="213" y="102" text-anchor="middle" font-size="10" fill="#ccc">of Protein</text>
      <g transform="translate(310 60) rotate(-90)">
        <circle r="42" fill="none" stroke="var(--carb)" stroke-width="16" stroke-dasharray="86 178"/>
        <circle r="42" fill="none" stroke="var(--protein)" stroke-width="16" stroke-dasharray="86 178" stroke-dashoffset="-88"/>
        <circle r="42" fill="none" stroke="var(--veg)" stroke-width="16" stroke-dasharray="86 178" stroke-dashoffset="-176"/>
        <circle r="32" fill="#b5b5b5"/>
      </g>
      <text x="310" y="64" text-anchor="middle" font-size="11" font-weight="700" fill="#fff">LUNCH</text>
      <path d="M370 45 Q395 25 420 45" fill="none" stroke="#4d7fd6" stroke-width="4" marker-end="url(#arrow)"/>
      <rect x="368" y="55" width="70" height="20" fill="var(--veg)"/>
      <text x="403" y="69" text-anchor="middle" font-size="11" font-weight="800" fill="#fff">SNACK</text>
      <text x="403" y="90" text-anchor="middle" font-size="10" fill="#ccc">1/2 Portion</text>
      <text x="403" y="102" text-anchor="middle" font-size="10" fill="#ccc">of Protein</text>
      <g transform="translate(500 60) rotate(-90)">
        <circle r="42" fill="none" stroke="var(--fat)" stroke-width="16" stroke-dasharray="86 178"/>
        <circle r="42" fill="none" stroke="var(--protein)" stroke-width="16" stroke-dasharray="86 178" stroke-dashoffset="-88"/>
        <circle r="42" fill="none" stroke="var(--veg)" stroke-width="16" stroke-dasharray="86 178" stroke-dashoffset="-176"/>
        <circle r="32" fill="#b5b5b5"/>
      </g>
      <text x="500" y="64" text-anchor="middle" font-size="11" font-weight="700" fill="#fff">DINNER</text>
    </svg>
    <p class="plan-copy">Fuel Your Heatwave Reset!<br>This plan isn't about starving yourself – it's about sculpting a lean,<br>toned physique by shredding fat while preserving muscle.</p>
  </section>

  <div class="beach" role="img" aria-label="Beach scene with sand, sea and tropical plants"></div>
  <p class="lead">Here's how to maximize your results:</p>

  <article class="tip t1"><h3>Eat Like a Champion</h3><p>Stick to this list as close as possible for maximum results, 7 Days A Week.</p></article>
  <article class="tip t2"><h3>Burn More Than You Consume</h3><p>This is the golden rule! You need to burn more calories than you consume to create a deficit and force your body to tap into fat stores for energy.</p></article>
  <article class="tip t3"><h3>Prioritize Protein</h3><p>Protein helps build and maintain muscle mass, which is crucial for boosting metabolism and burning more calories at rest.</p></article>
  <article class="tip t4"><h3>Maximize Sleep</h3><p>When sleep-deprived, your body produces more ghrelin (hunger hormone) and less leptin (satiety hormone). Aim for 7-8 hours of quality sleep nightly.</p></article>
  <article class="tip t5"><h3>Consistency is King/Queen</h3><p>Don't expect overnight results. Stick to your plan, track your progress, and celebrate small victories. Remember, slow and steady wins the shred race!</p></article>
</main>
</body>
</html>
```